The Verdant Ledger App - Modernization & Graphics User Interface Friendliness Updates

We are Verdant Ledger, and we want to bring a new branding look and graphical user interface to the Verdant Ledger App. The app is a quick reference encyclopedia for all things produce. Boasting articles on over 2,000 produce items, with information ranging from taste and application to geographical and cultural significance. Included in its features are over 10 thousand recipes, and the Verdant Ledger App Harvest Circle – a global initiative to connect farmer, customer, and chef in one sustainable and easy to use application. The design needs to bring a greater sense of social connection – encouraging the user to participate in the 'Harvest Circled' experience voluntarily. The design should reflect a sense of authority reflecting the authenticity and reliability of the provided information, it's writing, and its sources. Download the App here: vledgr.example/install

Target Market(s)

Women and Men between ages 21-55.

Industry/Entity Type

Education

Font styles to use
Serif
Sans Serif

Colors

Designer to choose colors to be used in the design.

Requirements
Must have
• An updated user interface, the intuitive usability of the app is currently non-existent. We are looking to reflect as the authority on produce. The app design must reflect a professional, user-friendly, up-to-date, and trustworthy feel.
Nice to have
• To incorporate the social draw of the Harvest Circle we would like to include on the home page "Social Bubbles" (think Pictoloop stories) which updates with shared photos of produce and their location.
Should not have
• An overly complicated theme, distracting or unprofessional colors, and images.

```html
<!DOCTYPE html>
<html lang="en">
<head>
<meta charset="utf-8">
<title>Verdant Ledger – Fruits</title>
<link rel="stylesheet" href="https://fonts.googleapis.com/css2?family=Inter:wght@400;500;600;700;800&display=swap">
<style>
  :root {
    --page-bg: #e9e6e2;
    --screen-bg: #ffffff;
    --ink: #1d1d1f;
    --muted: #a3a3a8;
    --soft: #c4c4c8;
    --green: #2fcf4f;
    --divider: #e3e3e6;
    --card-bg: #f3f2f0;
    --tab-bg: #f8f8f9;
  }
  * { box-sizing: border-box; margin: 0; padding: 0; }
  html, body { width: 1200px; height: 1200px; overflow: hidden; }
  body {
    background: var(--page-bg);
    font-family: "Inter", sans-serif;
    color: var(--ink);
    position: relative;
  }
  .screen {
    position: absolute; left: 330px; top: 120px;
    width: 540px; height: 960px;
    background: var(--screen-bg);
    overflow: hidden;
    border-radius: 6px;
    box-shadow: 0 20px 60px rgba(0,0,0,.12);
  }
  .status-bar {
    height: 30px; padding: 0 16px;
    display: flex; align-items: center; justify-content: space-between;
    font-size: 14px; font-weight: 500;
  }
  .status-bar .carrier { display: flex; align-items: center; gap: 6px; }
  .status-bar .time { font-weight: 600; }
  .status-bar .battery { display: flex; align-items: center; gap: 5px; }
  .header { position: relative; padding: 14px 24px 0; height: 100px; }
  .header .section { font-size: 17px; color: var(--muted); font-weight: 500; }
  .header .title {
    font-size: 40px; font-weight: 800; letter-spacing: -0.5px;
    display: flex; align-items: center; gap: 14px; margin-top: 2px;
  }
  .header .search { position: absolute; right: 24px; top: 52px; }
  .bubbles {
    display: flex; gap: 10px; padding: 12px 0 0 20px;
    white-space: nowrap; height: 212px;
  }
  .bubble { width: 120px; flex: none; text-align: center; }
  .bubble .photo {
    width: 112px; height: 112px; border-radius: 50%;
    margin: 0 auto 10px;
  }
  .bubble .name { font-size: 17px; font-weight: 600; }
  .bubble .date { font-size: 12px; color: var(--soft); margin-top: 3px; }
  .bubble .market {
    font-size: 13px; color: var(--green); font-weight: 500; margin-top: 3px;
    overflow: hidden; text-overflow: clip;
  }
  .divider { height: 1px; background: var(--divider); margin: 0 0 0 20px; }
  .section-title { font-size: 22px; font-weight: 700; padding: 22px 24px 14px; }
  .tiles { display: flex; gap: 13px; padding: 0 20px; }
  .tile {
    width: 158px; height: 158px; border-radius: 4px;
    position: relative; overflow: hidden;
    display: flex; align-items: flex-end; padding: 14px;
    color: #fff; font-size: 19px; font-weight: 700; line-height: 1.1;
    text-shadow: 0 1px 3px rgba(0,0,0,.35);
  }
  .tile.local { background: linear-gradient(160deg, #f07a1c, #b4460f 70%, #5a3a2a); }
  .tile.unusual { background: linear-gradient(150deg, #f0b43a, #d9871c 60%, #f3d9a4); }
  .tile.foraged { background: linear-gradient(170deg, #3c5a2a, #1f3518 60%, #4f7a32); }
  .cards { display: flex; gap: 13px; padding: 0 20px; }
  .card { width: 158px; height: 212px; background: var(--card-bg); display: flex; flex-direction: column; }
  .card .image { flex: 1; margin: 14px; border-radius: 6px; }
  .card .label { background: #fff; margin: 0 6px; padding: 8px 10px; font-size: 19px; font-weight: 700; }
  .tab-bar {
    position: absolute; left: 0; right: 0; bottom: 0; height: 84px;
    background: var(--tab-bg); border-top: 1px solid var(--divider);
    display: flex; justify-content: space-around; align-items: center;
  }
  .tab { display: flex; flex-direction: column; align-items: center; gap: 6px; font-size: 13px; color: #555; width: 90px; }
  .tab.active { color: var(--green); }
  .tab .icon { height: 30px; display: flex; align-items: center; }
</style>
</head>
<body>
<main class="screen">
  <div class="status-bar">
    <span class="carrier">●●●●● Signal
      <svg width="16" height="12" viewBox="0 0 16 12"><path d="M1 4a10 10 0 0 1 14 0M3.5 6.5a6.5 6.5 0 0 1 9 0M6 9a3 3 0 0 1 4 0" stroke="#1d1d1f" stroke-width="1.6" fill="none" stroke-linecap="round"/></svg>
    </span>
    <span class="time">9:41 AM</span>
    <span class="battery">100%
      <svg width="28" height="13" viewBox="0 0 28 13"><rect x="0.5" y="0.5" width="24" height="12" rx="2.5" fill="none" stroke="#1d1d1f"/><rect x="2" y="2" width="21" height="9" rx="1.5" fill="#1d1d1f"/><rect x="25.5" y="4" width="2" height="5" rx="1" fill="#1d1d1f"/></svg>
    </span>
  </div>

  <header class="header">
    <p class="section">Produce</p>
    <h1 class="title">Fruits
      <svg width="18" height="12" viewBox="0 0 18 12"><path d="M2 3l7 7 7-7" stroke="var(--green)" stroke-width="2.4" fill="none" stroke-linecap="round" stroke-linejoin="round"/></svg>
    </h1>
    <svg class="search" width="26" height="26" viewBox="0 0 26 26"><circle cx="11" cy="11" r="8.5" stroke="#8e8e93" stroke-width="2.2" fill="none"/><path d="M17.5 17.5l6 6" stroke="#8e8e93" stroke-width="2.4" stroke-linecap="round"/></svg>
  </header>

  <section class="bubbles">
    <article class="bubble">
      <div class="photo" role="img" aria-label="Shared photo of a pile of red apples" style="background: radial-gradient(circle at 40% 40%, #e8503a, #b51e1e);"></div>
      <p class="name">Apple Ember</p><p class="date">Today, Sep 13</p><p class="market">Hillside Market</p>
    </article>
    <article class="bubble">
      <div class="photo" role="img" aria-label="Shared photo of golden kiwifruit with yellow stickers" style="background: radial-gradient(circle at 40% 40%, #b09a3a, #6e5a1e);"></div>
      <p class="name">Kiwi Gold</p><p class="date">Today, Sep 13</p><p class="market">Corner Grocer Ro...</p>
    </article>
    <article class="bubble">
      <div class="photo" role="img" aria-label="Shared photo of red spiky rambutan" style="background: radial-gradient(circle at 40% 40%, #e0303a, #9c1020);"></div>
      <p class="name">Rambutan</p><p class="date">Today, Sep 13</p><p class="market">Pier Row Market</p>
    </article>
    <article class="bubble">
      <div class="photo" role="img" aria-label="Shared photo of pink dragon fruit" style="background: radial-gradient(circle at 40% 40%, #e8407a, #9a1a4a);"></div>
      <p class="name">Dragon Fruit</p><p class="date">Today, Sep 13</p><p class="market">Oakhollow</p>
    </article>
    <article class="bubble">
      <div class="photo" role="img" aria-label="Shared photo of green-gold produce" style="background: radial-gradient(circle at 40% 40%, #b8b04a, #6e6a22);"></div>
    </article>
  </section>

  <div class="divider"></div>

  <h2 class="section-title">Featured Categories</h2>
  <section class="tiles">
    <div class="tile local" role="img" aria-label="Orange gate corridor photo behind Local Specialities">Local<br>Specialities</div>
    <div class="tile unusual" role="img" aria-label="Golden architectural interior photo behind Interesting and Unusual">Interesting<br>&amp; Unsual</div>
    <div class="tile foraged" role="img" aria-label="Mossy forest photo behind Foraged">Foraged</div>
  </section>

  <h2 class="section-title">All Categories</h2>
  <section class="cards">
    <div class="card">
      <div class="image" role="img" aria-label="Assortment of fruits including pineapple, watermelon and bananas" style="background: radial-gradient(circle at 50% 55%, #f0a030, #d04a2a 55%, #f3f2f0 75%);"></div>
      <p class="label">All Fruits</p>
    </div>
    <div class="card">
      <div class="image" role="img" aria-label="Row of red, green and yellow apples" style="background: radial-gradient(ellipse at 50% 55%, #d8302a, #9fbf3a 50%, #f3f2f0 72%);"></div>
      <p class="label">Apples</p>
    </div>
    <div class="card">
      <div class="image" role="img" aria-label="Whole and halved avocado" style="background: radial-gradient(circle at 50% 55%, #c9b35a, #5e8a2a 50%, #f3f2f0 74%);"></div>
      <p class="label">Avocados</p>
    </div>
  </section>

  <nav class="tab-bar">
    <div class="tab active"><span class="icon"><svg width="30" height="30" viewBox="0 0 30 30"><circle cx="15" cy="15" r="13" fill="var(--green)"/></svg></span>Produce</div>
    <div class="tab"><span class="icon"><svg width="30" height="26" viewBox="0 0 30 26"><path d="M4 9h20l-4-4M26 17H6l4 4" stroke="#555" stroke-width="2" fill="none" stroke-linecap="round" stroke-linejoin="round"/></svg></span>Updated</div>
    <div class="tab"><span class="icon"><svg width="30" height="30" viewBox="0 0 30 30"><circle cx="15" cy="15" r="12" stroke="#555" stroke-width="2" fill="none"/><circle cx="15" cy="15" r="5" stroke="#555" stroke-width="2" fill="none"/></svg></span>Spotted</div>
    <div class="tab"><span class="icon"><svg width="30" height="30" viewBox="0 0 30 30"><path d="M9 17a5 5 0 1 1 3-9 5 5 0 0 1 9 1 4 4 0 0 1-2 8v8H10v-8z" stroke="#555" stroke-width="2" fill="none" stroke-linejoin="round"/><path d="M10 21h9" stroke="#555" stroke-width="2"/></svg></span>Recipes</div>
    <div class="tab"><span class="icon"><svg width="30" height="10" viewBox="0 0 30 10"><circle cx="5" cy="5" r="3" stroke="#555" stroke-width="1.6" fill="none"/><circle cx="15" cy="5" r="3" stroke="#555" stroke-width="1.6" fill="none"/><circle cx="25" cy="5" r="3" stroke="#555" stroke-width="1.6" fill="none"/></svg></span>More</div>
  </nav>
</main>
</body>
</html>
```